Brightwater Systems Website

I am starting an IT consulting business called Brightwater Systems. I recently completed a logo contest on ArtHive and am now looking to put together a basic website. I can provide text and content but am looking for a site design with layout and graphics. I am attaching my logo below. I was thinking of a dark blue and white theme for the website (similar to the logo). However, I am open to ideas. Graphics can be a mix of business and high tech as that is the image I am trying to convey. The site will be relatively simple and probably have only 3 - 5 pages (Home, About Us, Services, Contact, etc.)
Target Market(s)
United States commercial companies and government contractors
Industry/Entity Type
Consulting
Coding
Coded - Design and coding required
Number of Pages Required
4 page
Look and feel

```html
<!DOCTYPE html>
<html lang="en">
<head>
<meta charset="utf-8">
<title>Brightwater Systems</title>
<link rel="stylesheet" href="https://fonts.googleapis.com/css2?family=Josefin+Sans:wght@400;600;700&family=Lato:wght@400;700&family=Montserrat:wght@500;600;700&display=swap">
<style>
:root{
  --navy:#1f2940;
  --blue:#0a4ea3;
  --blue-bright:#1a74d9;
  --blue-soft:#2a6fc4;
  --ink:#222;
  --muted:#555;
  --white:#fff;
}
*{box-sizing:border-box;margin:0;padding:0}
html,body{width:1200px;height:3802px;overflow:hidden}
body{position:relative;background:var(--white);font-family:'Lato',sans-serif;color:var(--ink)}
.abs{position:absolute}
.site-header{left:0;top:0;width:1200px;height:106px;background:var(--navy)}
.brand{left:115px;top:28px;color:var(--white);font-family:'Montserrat',sans-serif}
.brand-name{font-size:27px;font-weight:600;letter-spacing:3px;display:flex;align-items:center;gap:8px}
.brand-dot{width:14px;height:14px;border-radius:50%;background:var(--blue-bright)}
.nav a{position:absolute;top:44px;font-family:'Montserrat',sans-serif;font-weight:700;font-size:15px;color:var(--white);text-decoration:none}
.nav a.active{color:var(--blue-bright)}
.btn-quote{left:922px;top:28px;width:167px;height:49px;border-radius:25px;background:var(--blue);color:var(--white);font:700 15px 'Montserrat',sans-serif;display:flex;align-items:center;justify-content:center}
.hero-photo{left:0;top:106px;width:1200px;height:703px;background:linear-gradient(120deg,#4a5a6c 0%,#9aa9b4 45%,#cfd8dc 70%,#6f8a70 100%)}
.hero-panel{left:89px;top:304px;width:472px;height:251px;background:rgba(16,86,180,.86);border-top-right-radius:90px;color:var(--white);padding:20px 22px}
.hero-title{font-family:'Josefin Sans',sans-serif;font-weight:600;font-size:54px;line-height:51px;letter-spacing:1px}
.hero-sub{font-family:'Josefin Sans',sans-serif;font-size:28px;margin-top:14px;letter-spacing:.5px}
.btn-outline-light{left:112px;top:483px;width:168px;height:45px;border:3px solid var(--white);border-radius:23px;color:var(--white);font:700 15px 'Montserrat',sans-serif;display:flex;align-items:center;justify-content:center}
.rule{height:3px;width:64px;background:var(--blue)}
.section-title{width:1200px;left:0;text-align:center;font-family:'Josefin Sans',sans-serif;font-size:42px;font-weight:400;color:var(--ink);letter-spacing:1.5px}
.lead{left:222px;width:756px;text-align:center;font-size:13px;line-height:23px;color:var(--muted)}
.svc-card{top:1045px;width:308px;height:401px;border-radius:34px;background:var(--white);box-shadow:0 0 14px rgba(0,0,0,.13);text-align:center}
.svc-card.featured{background:var(--blue);color:var(--white)}
.svc-icon{position:absolute;left:88px;top:21px;width:132px;height:132px;border-radius:50%;background:var(--blue);display:flex;align-items:center;justify-content:center}
.featured .svc-icon{background:var(--white)}
.svc-card h3{position:absolute;top:167px;width:100%;font-weight:400;font-size:21px}
.svc-card p{position:absolute;top:207px;left:28px;width:252px;font-size:13px;line-height:22.4px;color:var(--muted)}
.featured p{color:var(--white)}
.svc-card .more{position:absolute;top:342px;width:100%;font-size:16px;font-weight:700;color:var(--blue);text-decoration:underline}
.featured .more{color:var(--white)}
.about-text{left:112px;top:1625px;width:434px;font-size:13px;line-height:22.3px;color:var(--muted)}
.btn-solid{left:112px;top:1892px;width:168px;height:49px;border-radius:25px;background:var(--blue);color:var(--white);font:700 14px 'Montserrat',sans-serif;display:flex;align-items:center;justify-content:center}
.about-photo{left:599px;top:1540px;width:601px;height:398px;border-top-left-radius:50px;border-bottom-left-radius:50px;border-top:8px solid var(--blue);background:linear-gradient(110deg,#5a6b74,#b89a72 55%,#d8c3a8)}
.blog-card{width:316px;height:452px;background:var(--white);box-shadow:0 0 10px rgba(0,0,0,.18);text-align:center}
.blog-img{position:absolute;left:7px;top:7px;width:302px;height:210px;background:linear-gradient(135deg,#8a96a3,#c8b6a0 60%,#e5ddd3)}
.date{position:absolute;left:124px;top:181px;width:68px;height:68px;border-radius:50%;background:var(--blue);border:3px solid var(--white);color:var(--white);font-size:13px;font-weight:700;line-height:19px;padding-top:12px}
.blog-card h3{position:absolute;top:263px;width:100%;font-size:21px;font-weight:400}
.blog-card p{position:absolute;top:300px;left:30px;width:256px;font-size:13px;line-height:22.4px;color:var(--muted)}
.btn-outline{position:absolute;left:74px;top:379px;width:168px;height:48px;border:3px solid var(--blue);border-radius:24px;color:var(--blue);font:700 14px 'Montserrat',sans-serif;display:flex;align-items:center;justify-content:center}
.contact{left:0;top:2713px;width:1200px;height:714px;background:linear-gradient(180deg,#1a5fc0 0%,#1450a6 55%,#123f86 100%)}
.field-label{font-size:14px;color:var(--white)}
.field{background:var(--white);border-radius:4px;font-size:14px;color:#888;padding:14px 24px}
.btn-submit{left:518px;top:3284px;width:160px;height:47px;border:3px solid var(--white);border-radius:24px;color:var(--white);font:700 15px 'Montserrat',sans-serif;display:flex;align-items:center;justify-content:center}
.site-footer{left:0;top:3427px;width:1200px;height:375px;background:var(--navy);color:var(--white);font-family:'Montserrat',sans-serif}
.footer-h{font-size:15px;font-weight:700}
.footer-list{font-size:14px;line-height:28.4px;font-weight:500}
.social{width:30px;height:30px;border-radius:50%;background:var(--white);top:3584px}
.social.alt{background:var(--blue)}
.subscribe{left:803px;top:3606px;width:283px;height:50px;border-radius:25px;background:var(--white);border:2px solid #9ab;font-size:12px;color:#555;padding:16px 18px}
.send{left:1036px;top:3609px;width:46px;height:44px;border-radius:50%;background:var(--navy)}
</style>
</head>
<body>

<header class="abs site-header">
  <div class="abs brand"><div class="brand-name"><span class="brand-dot"></span>BRIGHTWATER</div><div style="font-size:11px;letter-spacing:10px;margin-top:4px">SYSTEMS</div></div>
  <nav class="nav">
    <a class="active" style="left:432px">HOME</a>
    <a style="left:512px">ABOUT US</a>
    <a style="left:627px">SERVICES</a>
    <a style="left:740px">CONTACT</a>
    <a style="left:849px">BLOG</a>
  </nav>
  <div class="abs btn-quote">GET A QUOTE</div>
</header>

<div class="abs hero-photo" role="img" aria-label="Business team meeting in a bright glass-walled conference room"></div>
<div class="abs hero-panel">
  <div class="hero-title">BRIGHTWATER<br>SYSTEMS</div>
  <div class="hero-sub">IT CONSULTING BUSINESS</div>
</div>
<div class="abs btn-outline-light">GET STARTED</div>
<svg class="abs" style="left:0;top:640px" width="1200" height="170" viewBox="0 0 1200 170">
  <path d="M0 40 Q600 330 1200 40 L1200 170 L0 170 Z" fill="#fff"/>
  <path d="M0 40 Q600 300 1200 40" fill="none" stroke="#0a4ea3" stroke-width="7"/>
  <circle cx="580" cy="79" r="6" fill="none" stroke="#fff" stroke-width="2"/>
  <circle cx="600" cy="79" r="8" fill="#2a6fc4" stroke="#fff" stroke-width="2"/>
  <circle cx="619" cy="79" r="6" fill="none" stroke="#fff" stroke-width="2"/>
</svg>

<div class="abs rule" style="left:568px;top:893px"></div>
<h2 class="abs section-title" style="top:912px">OUR SERVICES</h2>
<p class="abs lead" style="top:970px">Lorem ipsum dolor sit amet, consectetur adipiscing elit, sed do eiusmod tempor incididunt ut labore et dolore magna aliqua. Ut enim ad minim veniam, quis nostrud exercitation</p>

<div class="abs svc-card" style="left:111px">
  <div class="svc-icon"><svg width="72" height="72" viewBox="0 0 72 72" fill="none" stroke="#fff" stroke-width="2.5"><circle cx="36" cy="36" r="34"/><circle cx="38" cy="26" r="9"/><path d="M14 48h10l10 4h14l8-6M24 44l8-2h10"/></svg></div>
  <h3>Nemo enim ipsam</h3>
  <p>Lorem ipsum dolor sit amet, consecte tur adipiscing elit, sed do eiusmod tempor incididunt ut labore et dolore magna aliqua. Ut enim ad minim veniam, quis nostrud exercitation</p>
  <div class="more">Learn more ➔</div>
</div>
<div class="abs svc-card featured" style="left:447px">
  <div class="svc-icon"><svg width="72" height="72" viewBox="0 0 72 72" fill="none" stroke="#0a4ea3" stroke-width="2.5"><circle cx="36" cy="36" r="34"/><rect x="28" y="16" width="16" height="12"/><path d="M18 34h36M24 34v20M48 34v20M30 40h12v14"/><circle cx="20" cy="24" r="3"/><circle cx="52" cy="24" r="3"/></svg></div>
  <h3>Nemo enim ipsam</h3>
  <p>Lorem ipsum dolor sit amet, consecte tur adipiscing elit, sed do eiusmod tempor incididunt ut labore et dolore magna aliqua. Ut enim ad minim veniam, quis nostrud exercitation</p>
  <div class="more">Learn more ➔</div>
</div>
<div class="abs svc-card" style="left:781px">
  <div class="svc-icon"><svg width="72" height="72" viewBox="0 0 72 72" fill="none" stroke="#fff" stroke-width="2.5"><circle cx="36" cy="36" r="34"/><circle cx="32" cy="30" r="9"/><path d="M16 56c2-10 8-14 16-14s14 4 16 14M46 18l10 10M50 34l6-6"/></svg></div>
  <h3>Nemo enim ipsam</h3>
  <p>Lorem ipsum dolor sit amet, consecte tur adipiscing elit, sed do eiusmod tempor incididunt ut labore et dolore magna aliqua. Ut enim ad minim veniam, quis nostrud exercitation</p>
  <div class="more">Learn more ➔</div>
</div>

<div class="abs rule" style="left:112px;top:1547px"></div>
<h2 class="abs section-title" style="left:112px;width:auto;top:1566px;text-align:left">ABOUT US</h2>
<p class="abs about-text">Lorem ipsum dolor sit amet, consectetur adipiscing elit, sed do eiusmod tempor incididunt ut labore et dolore magna aliqua. Ut enim ad minim veniam, quis nostrud exercitation ullamco laboris nisi ut aliquip ex ea commodo consequat. Duis aute irure dolor in reprehenderit in voluptate velit esse cillum dolore eu fugiat nulla pariatur. Excepteur sint occaecat cupidatat non proident, sunt in culpa qui officia deserunt mollit anim id est laborum. Lorem ipsum dolor sit amet, consectetur adipiscing elit, sed do eiusmod tempor incididunt ut labore et dolore magna aliqua. Ut enim ad minim veniam, quis nostrud exercitation ullamco laboris nisi ut aliquip ex ea commodo consequat. Duis aute irure dolor in reprehenderit in voluptate velit esse cillum dolore eu fugiat nulla pariatur.</p>
<div class="abs btn-solid">LEARN MORE ➔</div>
<div class="abs about-photo" role="img" aria-label="Smiling consultant with colleagues working on laptops at a wooden table"></div>

<div class="abs rule" style="left:568px;top:2045px"></div>
<h2 class="abs section-title" style="top:2062px">LATEST BLOG</h2>

<div class="abs blog-card" style="left:111px;top:2158px">
  <div class="blog-img" role="img" aria-label="Colleagues gathered around a laptop"></div>
  <div class="date">Jan<br>2021</div>
  <h3>Lorem ipsum dolor</h3>
  <p>Lorem ipsum dolor sit amet, consectetur adipiscing elit, sed do eiusmod tempor incididun</p>
  <div class="btn-outline">LEARN MORE ➔</div>
</div>
<div class="abs blog-card" style="left:441px;top:2140px">
  <div class="blog-img" role="img" aria-label="Two professionals reviewing notes at a desk"></div>
  <div class="date">Jan<br>2021</div>
  <h3>Lorem ipsum dolor</h3>
  <p>Lorem ipsum dolor sit amet, consectetur adipiscing elit, sed do eiusmod tempor incididun</p>
  <div class="btn-outline">LEARN MORE ➔</div>
</div>
<div class="abs blog-card" style="left:773px;top:2158px">
  <div class="blog-img" role="img" aria-label="Team discussing a project on a laptop in an office"></div>
  <div class="date">Jan<br>2021</div>
  <h3>Lorem ipsum dolor</h3>
  <p>Lorem ipsum dolor sit amet, consectetur adipiscing elit, sed do eiusmod tempor incididun</p>
  <div class="btn-outline">LEARN MORE ➔</div>
</div>

<section class="abs contact" role="img" aria-label="Blue-toned city skyline at dusk behind the contact form"></section>
<svg class="abs" style="left:0;top:2712px" width="1200" height="135" viewBox="0 0 1200 135">
  <path d="M0 0 L1200 0 L1200 130 Q600 -130 0 130 Z" fill="#fff"/>
  <path d="M0 125 Q600 -120 1200 125" fill="none" stroke="#0a4ea3" stroke-width="7"/>
</svg>
<div class="abs rule" style="left:568px;top:2790px;background:#fff"></div>
<h2 class="abs section-title" style="top:2808px;color:#fff">CONTACT US</h2>
<div class="abs field-label" style="left:236px;top:2882px">First name</div>
<div class="abs field-label" style="left:613px;top:2882px">Last name</div>
<div class="abs field" style="left:236px;top:2915px;width:350px;height:50px">John....|</div>
<div class="abs field" style="left:613px;top:2915px;width:351px;height:50px">John....|</div>
<div class="abs field-label" style="left:236px;top:2985px">Phone</div>
<div class="abs field-label" style="left:613px;top:2985px">Email address</div>
<div class="abs field" style="left:236px;top:3019px;width:350px;height:50px"></div>
<div class="abs field" style="left:613px;top:3019px;width:351px;height:50px"></div>
<div class="abs field-label" style="left:236px;top:3087px">Message</div>
<div class="abs field" style="left:236px;top:3120px;width:725px;height:144px">Text here...|</div>
<div class="abs btn-submit">SUBMIT</div>

<footer class="abs site-footer"></footer>
<div class="abs" style="left:128px;top:3518px;color:#fff;font-family:'Montserrat',sans-serif">
  <div style="font-size:21px;font-weight:600;letter-spacing:2px;display:flex;align-items:center;gap:6px"><span style="width:10px;height:10px;border-radius:50%;background:#1a74d9"></span>BRIGHTWATER</div>
  <div style="font-size:9px;letter-spacing:8px;margin-top:3px">SYSTEMS</div>
</div>
<div class="abs social" style="left:130px"></div>
<div class="abs social alt" style="left:164px"></div>
<div class="abs social" style="left:199px"></div>
<div class="abs social" style="left:233px"></div>

<div class="abs footer-h" style="left:393px;top:3508px;color:#fff;font-family:'Montserrat',sans-serif">QUICK LINKS</div>
<div class="abs" style="left:393px;top:3535px;width:78px;height:2px;background:#fff"></div>
<div class="abs footer-list" style="left:393px;top:3540px;color:#fff;font-family:'Montserrat',sans-serif">Home<br>About us<br>Services<br>Blog<br>Contact us</div>

<div class="abs footer-h" style="left:559px;top:3508px;color:#fff;font-family:'Montserrat',sans-serif">CONTACT US</div>
<div class="abs footer-list" style="left:559px;top:3540px;color:#fff;font-family:'Montserrat',sans-serif">✆ 888-888-8888<br>✉ info@brightwatersys.com<br>⚲ 1234 location sed lomer<br>&nbsp;&nbsp;&nbsp;sed xxxx NY xxxx</div>

<div class="abs footer-h" style="left:809px;top:3508px;color:#fff;font-family:'Montserrat',sans-serif">SUBSCRIBE TO OUR BLOG</div>
<div class="abs footer-list" style="left:809px;top:3540px;color:#fff;font-family:'Montserrat',sans-serif">Sign up today to get resources on how to<br>attract and retain more customers!</div>
<div class="abs subscribe">Email Address</div>
<div class="abs send"><svg width="46" height="44" viewBox="0 0 46 44"><path d="M14 23 L32 14 L26 31 L23 24 Z" fill="#fff"/></svg></div>

<div class="abs" style="left:111px;top:3728px;color:#fff;font:500 14px 'Montserrat',sans-serif">Copyright © 2021. All Rights Reserved</div>
<div class="abs" style="left:834px;top:3728px;color:#fff;font:500 14px 'Montserrat',sans-serif">Terms and Conditions | Privacy Policy</div>

</body>
</html>
```